Banner to be displayed at local Farmers Market Booth.

Graphic Design Brief: Farmers Market Banner Contest

Project Overview:We are seeking talented graphic designers to create a visually appealing banner for our booth at the local farmers market. Our company specializes in healthy, all-natural dog and cat treats, and we want a banner that captures our brand identity while drawing in pet owners who value quality and nutrition for their furry friends.

Banner Specifications:

Size: 24 inches x 60 inches (Horizontal orientation) 24" High X 60 wide

Theme: Vintage/Retro

Style: Warm, inviting, nostalgic with a touch of rustic charm

Colors: Earthy, muted tones such as warm browns, soft greens, and creamy yellows. Pops of red or blue may be used sparingly for accents. OR Black and White with gray scales. Would like to see both

Typography: Retro-style fonts that are readable and align with the vintage aesthetic.

Key Elements to Include: website (www.dorvalfinest.net)

Company Name: Dorval's Finest

Tagline: " Just Good Stuff "
Imagery: Illustrations or stylized graphics of happy dogs and cats, possibly interacting with treats.

Emphasis on Natural Ingredients: Icons or design elements that subtly suggest freshness and quality (e.g., leaves, wheat, bones, or paw prints).

Farmers Market Appeal: A design that blends well with the artisanal, handmade, and farm-fresh atmosphere of the market.

Design Considerations:

The banner should be easily readable from a distance.

A balanced composition that doesn't feel overcrowded.

Should evoke trust and warmth while maintaining a professional look.

Avoid overly modern or sleek elements that don’t align with the vintage aesthetic.

Submission Requirements:

High-resolution digital file in PDF or AI format.

CMYK color mode for printing purposes.

Must include a mockup or preview of how it would look in a real farmers market setting.

We look forward to seeing your creative interpretations of our brand! If you have any questions, feel free to reach out.

Font styles to use
Other font styles liked:

Requirements
Nice to have
• Retro/Vintage,playful BUT NOT whimsical

```html
<!DOCTYPE html>
<html lang="en">
<head>
<meta charset="utf-8">
<title>Dorval's Finest – Just Good Stuff banner</title>
<link href="https://fonts.googleapis.com/css2?family=League+Spartan:wght@700&family=Oswald:wght@500&display=swap" rel="stylesheet">
<style>
  :root {
    --page: #e8eaec;
    --banner: #fbfbf9;
    --ink: #262626;
    --ink-soft: #3a3a3a;
    --sketch-light: #e2e2e0;
    --sketch-mid: #cfcfcc;
    --faint-mark: #dadad8;
    --ribbon: #a3cf6e;
    --ribbon-dark: #8cbb58;
    --on-ribbon: #ffffff;
  }
  * { margin: 0; padding: 0; box-sizing: border-box; }
  html, body { width: 841px; height: 1200px; overflow: hidden; }
  body { background: var(--page); position: relative; }

  .banner {
    position: absolute;
    left: 20px; top: 441px;
    width: 801px; height: 318px;
    background: var(--banner);
    overflow: hidden;
    box-shadow: 0 2px 10px rgba(0,0,0,.12);
  }
  .illustration { position: absolute; border-radius: 6px; }
  .farm-scene {
    left: 174px; top: 14px; width: 280px; height: 104px;
    background: linear-gradient(180deg, var(--sketch-light) 0%, var(--sketch-mid) 100%);
  }
  .tractor-scene {
    left: 462px; top: 14px; width: 305px; height: 104px;
    background: linear-gradient(180deg, var(--sketch-light) 0%, var(--sketch-mid) 100%);
  }
  .dog-sketch {
    left: 53px; top: 182px; width: 172px; height: 132px;
    background: radial-gradient(ellipse at 50% 55%, var(--sketch-mid), var(--sketch-light) 75%);
  }
  .cat-sketch {
    left: 574px; top: 192px; width: 127px; height: 122px;
    background: radial-gradient(ellipse at 50% 55%, var(--sketch-mid), var(--sketch-light) 75%);
  }

  .faint-name {
    position: absolute;
    left: 14px; top: 110px;
    font-family: 'League Spartan', sans-serif;
    font-weight: 700;
    font-size: 46px;
    color: var(--faint-mark);
  }

  .brand-mark {
    position: absolute;
    left: 50%; top: 6px;
    transform: translateX(-50%);
    display: flex; align-items: center; gap: 8px;
    background: var(--banner);
    padding: 6px 12px;
    border-radius: 40px;
  }
  .brand-dot {
    width: 30px; height: 30px; border-radius: 50%;
    background: var(--ink);
  }
  .brand-name {
    font-family: 'League Spartan', sans-serif;
    font-weight: 700;
    font-size: 26px;
    color: var(--ink);
    line-height: 1;
    padding-top: 4px;
  }

  .tagline {
    position: absolute;
    left: 0; right: 0; top: 126px;
    text-align: center;
    font-family: 'League Spartan', sans-serif;
    font-weight: 700;
    font-size: 84px;
    line-height: 66px;
    letter-spacing: 1px;
    color: var(--ink);
    text-transform: uppercase;
  }

  .web-ribbon {
    position: absolute;
    left: 244px; top: 262px;
    width: 311px; height: 34px;
  }
  .web-ribbon svg { position: absolute; inset: 0; }
  .web-address {
    position: absolute; inset: 0;
    display: flex; align-items: center; justify-content: center;
    font-family: 'Oswald', sans-serif;
    font-weight: 500;
    font-size: 17px;
    letter-spacing: 4px;
    color: var(--on-ribbon);
    text-transform: uppercase;
  }
</style>
</head>
<body>
  <main class="banner">
    <div class="illustration farm-scene" role="img" aria-label="Pencil sketch of a barn, silos, a cow and chickens under soft clouds"></div>
    <div class="illustration tractor-scene" role="img" aria-label="Pencil sketch of a vintage tractor in a field with chickens and clouds"></div>

    <div class="faint-name" aria-hidden="true">Dorval's</div>

    <div class="brand-mark">
      <span class="brand-dot"></span>
      <span class="brand-name">Dorval's</span>
    </div>

    <h1 class="tagline">Just Good<br>Stuff</h1>

    <div class="illustration dog-sketch" role="img" aria-label="Pencil sketch of a dog lying down and looking up"></div>
    <div class="illustration cat-sketch" role="img" aria-label="Pencil sketch of a fluffy cat walking with its tail raised"></div>

    <div class="web-ribbon">
      <svg viewBox="0 0 311 34" width="311" height="34" aria-hidden="true">
        <polygon points="0,3 22,3 22,31 0,31 9,17" fill="var(--ribbon-dark)"/>
        <polygon points="311,3 289,3 289,31 311,31 302,17" fill="var(--ribbon-dark)"/>
        <rect x="16" y="0" width="279" height="34" fill="var(--ribbon)"/>
        <circle cx="30" cy="17" r="2.5" fill="var(--on-ribbon)"/>
        <circle cx="281" cy="17" r="2.5" fill="var(--on-ribbon)"/>
      </svg>
      <span class="web-address">dorvalfinest.net</span>
    </div>
  </main>
</body>
</html>
```